We need a flyer (size Din A4, folded, see image).
Attached you will find the content with a rough arrangement.
The inner part will contain some Q&A, we have sketched two possible arrangements of the content.
We are looking for a professional design and a good, clean layout.
Maybe you have some ideas how to arrange the content in a smarter way, we are open for suggestions.
The draft contains no images. It would be good to have an explaining image at least on the front of the flyer.
Attached you will find some stock photos we are using on our website, but you can also propose your own images.
If useful, here is our webpage:
https://vorn-strom.de/
and the landing page for the offering
https://vorn-strom. en/charging-solutions-for-house-management-and-routes/
(this landing page is not professionally designed, so feel free to create a better design for the flyer)
Our target group are real estate managers/facility managers of larger apartment buildings.
The offering is: full-serviced solutions for charging infrastructure for electric cars at the parking lots for residents.
Please do not hesitate to contact me, if you need further information.
Target Market(s)
Professionals in real estate management, facility management
Industry/Entity Type
charging infrastructures for electric cars, focus: appartment buildings

```html
<!DOCTYPE html>
<html lang="de">
<head>
<meta charset="utf-8">
<title>vorn-strom Flyer</title>
<link href="https://fonts.googleapis.com/css2?family=Orbitron:wght@500;700&family=Arimo:wght@400;700&display=swap" rel="stylesheet">
<style>
:root{
  --bg:#ece9e6;
  --pink:#e0189a;
  --magenta:#c21fa8;
  --purple:#8e35b8;
  --violet:#6b3fa8;
  --deep:#4b2f86;
  --blue-dark:#1b2f78;
  --blue:#3a7be0;
  --sky:#cfe2fb;
  --paper:#f6f6f7;
  --ink:#2c2c34;
  --white:#ffffff;
  --heading:"Orbitron",sans-serif;
  --body:"Arimo",Arial,sans-serif;
}
*{margin:0;padding:0;box-sizing:border-box}
html,body{width:1191px;height:1200px;overflow:hidden;background:var(--bg);font-family:var(--body);color:var(--ink)}
.spread{position:absolute;left:175px;width:840px;height:580px;overflow:hidden;box-shadow:0 6px 18px rgba(0,0,0,.18)}
.spread--outside{top:10px}
.spread--inside{top:610px}
.spread>svg.backdrop{position:absolute;inset:0}
.panel{position:absolute;top:0;width:280px;height:580px}
.panel--1{left:0}.panel--2{left:280px}.panel--3{left:560px}
.fold{position:absolute;top:0;width:0;height:580px;border-left:1px dashed rgba(255,255,255,.35)}

/* outside – features */
.feature{position:absolute;left:22px;display:flex;gap:12px;align-items:flex-start;width:240px}
.feature svg{flex:0 0 24px}
.feature p{font-size:8.5px;line-height:1.5;color:var(--ink)}
.invite{position:absolute;left:22px;top:470px;color:var(--white);font-size:8.5px;line-height:1.6;width:240px}
.invite ul{list-style:none;margin-top:10px}
.invite li{font-weight:700;padding-left:16px;position:relative}
.invite li::before{content:"";position:absolute;left:2px;top:5px;width:4px;height:4px;border-radius:50%;background:#f09ad8}

/* outside – contact */
.cta{position:absolute;top:40px;left:0;width:280px;text-align:center}
.cta h3{font-size:10px;font-weight:700;color:var(--pink);line-height:1.3;letter-spacing:.02em}
.cta hr{width:90px;margin:8px auto;border:0;border-top:1px solid var(--deep)}
.cta .line{font-size:10px;color:var(--ink);line-height:1.35;display:flex;justify-content:center;align-items:center;gap:6px}
.cta .pitch{margin:45px auto 0;width:180px;font-size:7px;font-weight:700;line-height:1.4;color:var(--ink)}
.seal{position:absolute;left:85px;top:240px;width:110px;height:110px;border-radius:50%;display:flex;align-items:center;justify-content:center}
.brand{font-family:var(--body);font-weight:400;color:var(--white);font-size:13px}
.imprint{position:absolute;top:385px;left:0;width:280px;text-align:center;color:var(--white);font-size:8px;line-height:1.4}
.imprint .icon{display:block;margin:8px auto 3px}

/* outside – cover */
.cover-brand{position:absolute;top:30px;left:40px;display:flex;align-items:center;gap:8px}
.cover-brand .dot{width:12px;height:12px;border-radius:50%;background:var(--magenta)}
.cover-brand .brand{color:var(--ink);font-size:14px}
.cover-title{position:absolute;left:18px;top:320px;color:#ecdcf3;font-family:var(--heading)}
.cover-title .big{font-size:22px;font-weight:700;display:block;letter-spacing:.02em}
.cover-title .small{font-size:9.5px;font-weight:500;display:block;line-height:1.1;color:#f3e6f7}
.cover-title .sub{font-family:var(--body);font-size:8px;font-weight:700;color:#f3e6f7;display:block;margin-top:4px}
.cover-copy{position:absolute;left:18px;top:445px;width:250px;color:#e6cfee;font-size:5.8px;line-height:1.35}
.cover-copy p{margin-bottom:5px}

/* inside */
.inside-title{position:absolute;top:22px;font-family:var(--heading);font-weight:700;font-size:13.5px;line-height:1.2;color:#f4e6f8;letter-spacing:.02em}
.inside-title--problem{left:16px}
.inside-title--solution{left:298px}
.rule{position:absolute;top:64px;left:16px;width:180px;border-top:1px solid rgba(255,255,255,.5)}
.qa{position:absolute;left:0;width:560px;display:grid;grid-template-columns:280px 280px}
.qa .q{display:flex;align-items:center}
.q-box{margin-left:16px;width:196px;background:rgba(55,40,110,.65);color:var(--white);font-size:7.5px;font-weight:700;line-height:1.4;padding:7px 18px 7px 8px;clip-path:polygon(0 0,calc(100% - 10px) 0,100% 50%,calc(100% - 10px) 100%,0 100%)}
.a-box{margin-left:-12px;width:270px;background:rgba(180,40,170,.45);color:#f7e8f7;font-size:6.6px;line-height:1.45;padding:6px 14px 6px 14px}
.a-box p+p{margin-top:7px}

.steps-title{position:absolute;top:22px;left:16px;font-family:var(--heading);font-weight:700;font-size:13.5px;line-height:1.25;color:var(--ink)}
.step{position:absolute;left:16px;width:250px}
.step .head{display:flex;align-items:center;gap:18px}
.step h4{font-size:14px;font-weight:700;color:var(--magenta)}
.step ul{list-style:none;margin-top:8px;font-size:7.5px;line-height:1.4;color:var(--ink)}
.step li::before{content:"• "}
</style>
</head>
<body>

<!-- ===== Outside ===== -->
<section class="spread spread--outside">
  <svg class="backdrop" width="840" height="580" viewBox="0 0 840 580">
    <defs>
      <linearGradient id="wave" x1="0" y1="1" x2="1" y2="0">
        <stop offset="0" stop-color="#e0189a"/><stop offset=".55" stop-color="#a32db4"/><stop offset="1" stop-color="#8e35b8"/>
      </linearGradient>
      <linearGradient id="photoTone" x1="0" y1="0" x2="1" y2="1">
        <stop offset="0" stop-color="#dbe8fb"/><stop offset=".45" stop-color="#7fb0f0"/><stop offset="1" stop-color="#1b2f78"/>
      </linearGradient>
      <radialGradient id="sealTone" cx=".5" cy=".35" r=".7">
        <stop offset="0" stop-color="#c53fb8"/><stop offset="1" stop-color="#7b3fb0"/>
      </radialGradient>
    </defs>
    <rect width="840" height="580" fill="#f6f6f7"/>
    <rect x="280" y="0" width="560" height="360" fill="url(#photoTone)" role="img" aria-label="Foto: Ladestecker mit blau leuchtendem Ring an einem Elektroauto"/>
    <path d="M0,375 C150,340 260,285 420,255 C600,225 740,270 840,320 L840,580 L0,580 Z" fill="#7a4fc0"/>
    <path d="M0,390 C150,355 260,300 420,270 C600,240 740,285 840,335 L840,580 L0,580 Z" fill="url(#wave)"/>
    <circle cx="185" cy="270" r="55" fill="#9a3fc0"/>
    <circle cx="185" cy="270" r="51" fill="#3b3f4a" role="img" aria-label="Foto: Elektroauto in einer Tiefgarage an der Ladestation"/>
    <circle cx="155" cy="375" r="68" fill="#9a3fc0"/>
    <circle cx="155" cy="375" r="64" fill="#a79b92" role="img" aria-label="Foto: Ladekabel mit Stecker, im Hintergrund eine Bewohnerin"/>
    <circle cx="420" cy="295" r="56" fill="url(#sealTone)"/>
  </svg>
  <span class="fold" style="left:280px"></span>
  <span class="fold" style="left:560px"></span>

  <div class="panel panel--1">
    <div class="feature" style="top:32px">
      <svg width="24" height="26" viewBox="0 0 24 26"><rect x="2" y="2" width="16" height="20" fill="none" stroke="#5a3fa0" stroke-width="1.8"/><path d="M6 8h8M6 12h8M6 16h5" stroke="#5a3fa0" stroke-width="1.5"/><circle cx="19" cy="20" r="4" fill="#fff" stroke="#5a3fa0" stroke-width="1.5"/></svg>
      <p>Zukunftsfähig durch flexibles Abrechnungsmodell für verschiedene Einsatzmöglichkeiten.</p>
    </div>
    <div class="feature" style="top:90px">
      <svg width="24" height="26" viewBox="0 0 24 26"><path d="M18 3v6M14 6h8M18 9c0 6-12 3-12 9v4" fill="none" stroke="#5a3fa0" stroke-width="1.8"/><rect x="3" y="20" width="6" height="5" fill="#5a3fa0"/></svg>
      <p>Leichter, schneller Einstieg in das Thema, unkomplizierte und professionelle Abwicklung</p>
    </div>
    <div class="feature" style="top:142px">
      <svg width="24" height="24" viewBox="0 0 24 24"><path d="M3 16l3-6h12l3 6v5H3z" fill="#5a3fa0"/><circle cx="7" cy="17" r="1.5" fill="#fff"/><circle cx="17" cy="17" r="1.5" fill="#fff"/><path d="M12 1l-3 5h4l-2 4" fill="none" stroke="#5a3fa0" stroke-width="1.5"/></svg>
      <p>Aufbau und Betrieb von Ladelösungen speziell für Hausverwaltungen und WEGs</p>
    </div>
    <div class="invite">
      <p>Bieten Sie ihren Bewohnern Lademöglichkeiten für ihre Elektrofahrzeuge –</p>
      <ul><li>einfach,</li><li>unkompliziert und</li><li>zukunftsfähig.</li></ul>
    </div>
  </div>

  <div class="panel panel--2">
    <div class="cta">
      <h3>JETZT BERATUNGSGESPRÄCH<br>ANFORDERN UNTER:</h3>
      <hr>
      <p class="line"><svg width="9" height="9" viewBox="0 0 10 10"><circle cx="5" cy="5" r="4.5" fill="#e0189a"/></svg>https://vorn-strom.de/WEG</p>
      <p class="line">oder</p>
      <p class="line"><svg width="9" height="9" viewBox="0 0 10 10"><circle cx="5" cy="5" r="4.5" fill="#e0189a"/><path d="M3 3l1 0 1 2-1 1 1 1 1-1 2 1v1c-3 0-5-2-5-5z" fill="#fff"/></svg>08152 / 123 45 67</p>
      <p class="pitch">Als Anbieter von Full-Service-Lösungen ermöglicht vorn-strom eine für Immobilienbesitzer/-verwalter einfache und ausbaubare Lösung, die alle Bereiche abdeckt.</p>
    </div>
    <div class="seal"><span class="brand">vorn-strom.de</span></div>
    <div class="imprint">
      <svg class="icon" width="8" height="10" viewBox="0 0 8 10"><path d="M4 0a4 4 0 0 1 4 4c0 3-4 6-4 6S0 7 0 4a4 4 0 0 1 4-4z" fill="#f3c9ec"/><circle cx="4" cy="4" r="1.5" fill="#a32db4"/></svg>
      <p>vorn-strom GmbH<br>Lindenweg 14<br>82211 Herrsching</p>
      <p style="margin-top:12px">HRB 198765<br>Amtsgericht München<br>Geschäftsführung: Marie Falkner</p>
      <svg class="icon" width="10" height="8" viewBox="0 0 10 8"><rect width="10" height="8" rx="1" fill="#f3c9ec"/><path d="M0 1l5 4 5-4" fill="none" stroke="#a32db4"/></svg>
      <p>info@vorn-strom.de</p>
      <svg class="icon" width="9" height="9" viewBox="0 0 10 10"><path d="M2 1h2l1 3-1.5 1a6 6 0 0 0 2.5 2.5L7 6l3 1v2c-5 0-9-4-9-8z" fill="#f3c9ec"/></svg>
      <p>08152 / 123 45 67</p>
    </div>
  </div>

  <div class="panel panel--3">
    <div class="cover-brand"><span class="dot"></span><span class="brand">vorn-strom.de</span></div>
    <h1 class="cover-title">
      <span class="big">Flexible</span>
      <span class="small">Ladeinfrastrukturen<br>für die<br>Elektromobilität für<br>Mieter und</span>
      <span class="big">Eigentümer</span>
      <span class="sub">einfach, unkompliziert und zukunftsfähig</span>
    </h1>
    <div class="cover-copy">
      <p>Bauträger und Hausverwaltungen/WEGs, die einfach zukunftsfähige Ladelösungen für Ihre Stellplätze benötigen</p>
      <p>Hausverwaltungen werden von Mietern und Eigentümern immer öfter konfrontiert mit dem Wunsch nach Lademöglichkeiten für die Bewohner.</p>
      <p>Zudem verlangt das neue Gebäude-Elektromobilitäts-infrastruktur Gesetz (GEIG) den Ausbau der Ladeinfrastruktur bei der Renovierung der TG.</p>
    </div>
  </div>
</section>

<!-- ===== Inside ===== -->
<section class="spread spread--inside">
  <svg class="backdrop" width="840" height="580" viewBox="0 0 840 580">
    <defs>
      <linearGradient id="insideTone" x1="0" y1="1" x2="1" y2="0">
        <stop offset="0" stop-color="#e0189a"/><stop offset=".5" stop-color="#a32db4"/><stop offset="1" stop-color="#7b3fb0"/>
      </linearGradient>
    </defs>
    <rect width="560" height="580" fill="url(#insideTone)"/>
    <rect x="280" width="280" height="580" fill="rgba(90,50,150,.25)"/>
    <rect x="560" width="280" height="580" fill="#f6f6f7"/>
  </svg>
  <span class="fold" style="left:280px"></span>

  <h2 class="inside-title inside-title--problem">Problem /<br>Fragestellung</h2>
  <span class="rule"></span>
  <h2 class="inside-title inside-title--solution">Der Lösungsansatz<br>von vorn-strom</h2>

  <div class="qa" style="top:100px">
    <div class="q"><div class="q-box">Ein Bewohner will eine Wallbox – was tun?</div></div>
    <div class="a-box"><p>Mieter/Eigentümer hat nach WoMoG Anspruch auf eine Wallbox.<br>Die Hausverwaltung darf den Wunsch nicht verhindern, darf aber - und sollte - Vorgaben machen, um eine nachhaltige Gesamtlösung sicherzustellen.<br>vorn-strom liefert diese Vorgaben, damit Installation und weiterer Ausbau der Ladeinfrastruktur geordnet erfolgen kann.</p></div>
  </div>
  <div class="qa" style="top:192px">
    <div class="q"><div class="q-box">Der Stromanschluss reicht nicht, wenn alle Bewohner eine Wallbox wollen!</div></div>
    <div class="a-box"><p>Mit Hilfe des Last-Managements von vorn-strom lässt sich die verfügbare Strom-Kapazität intelligent steuern, so dass der Hausanschluss in der Regel langfristig ausreicht.</p></div>
  </div>
  <div class="qa" style="top:258px">
    <div class="q"><div class="q-box">Sind die Vorabprüfung und der Einbau von Ladeinfrastruktur teuer? Wie überzeugt man die WEG von den Kosten?</div></div>
    <div class="a-box"><p>Bei der Lösung von vorn-strom werden nur aktuell benötigte Wallboxen aufgebaut - erforderliche Investitionen erfolgen schrittweise nach Bedarf.<br>Mit dem optionalen Mietmodell entstehen der WEG keine oder nur geringe Kosten, hier können die Kosten größtenteils auf die Nutzer der Wallboxen verlagert werden.</p></div>
  </div>
  <div class="qa" style="top:350px">
    <div class="q"><div class="q-box">Die Bewohner haben keine fest zugeordneten Stellplätze</div></div>
    <div class="a-box"><p>Der Anschluss an den Wohnungszähler des jeweiligen Mieters/Eigentümers ist nicht notwendig. vorn-strom rechnet auf Wunsch mit jedem Mieter direkt dessen Ladestromverbrauch ab.</p></div>
  </div>
  <div class="qa" style="top:414px">
    <div class="q"><div class="q-box">Wer kann helfen, eine professionelle und zukunftsfähige Ladeinfrastruktur zu entwickeln?</div></div>
    <div class="a-box"><p>vorn-strom ist Spezialist für Ladeinfrastruktur, und kennt sich neben den speziellen technischen Lösungen auch mit rechtlichen Fragestellungen und Abrechnungslösungen aus.</p><p>Neben der Umsetzung unterstützt vorn-strom die Hausverwaltungen bei technischen und juristischen Fragen, um zusammen mit der WEG eine optimale Lösung aufzubauen.</p></div>
  </div>
  <div class="qa" style="top:525px">
    <div class="q"><div class="q-box">Bei uns wurden bereits Wallboxen von einzelnen Mietern installiert, was nun?</div></div>
    <div class="a-box"><p>In vielen Fällen kann Hardware anderer Hersteller in die Abrechnungslösung von vorn-strom integriert werden.</p></div>
  </div>

  <div class="panel panel--3">
    <h2 class="steps-title">Die Schritte zur<br>Ladeinfrastruktur<br>in Ihrem Objekt:</h2>
    <div class="step" style="top:110px">
      <div class="head"><svg width="28" height="28" viewBox="0 0 28 28"><path d="M4 20l3-7h14l3 7v5H4z" fill="#a32db4"/><circle cx="9" cy="21" r="1.6" fill="#fff"/><circle cx="19" cy="21" r="1.6" fill="#fff"/><path d="M14 2v8M11 4v3h6V4" stroke="#a32db4" stroke-width="1.6" fill="none"/></svg><h4>Erstprüfung</h4></div>
      <ul><li>Machbarkeitsprüfung</li><li>Abschätzung, Planung nächster Schritte</li></ul>
    </div>
    <div class="step" style="top:200px">
      <div class="head"><svg width="28" height="28" viewBox="0 0 28 28"><rect x="5" y="3" width="18" height="22" fill="none" stroke="#a32db4" stroke-width="2"/><path d="M5 10h18M11 10v15M17 10v15M5 17h18" stroke="#a32db4" stroke-width="1.6"/></svg><h4>Konzeption</h4></div>
      <ul><li>Planung der Anlage</li><li>Abstimmung Netzbetreiber</li><li>Kostenkalkulation</li></ul>
    </div>
    <div class="step" style="top:300px">
      <div class="head"><svg width="28" height="28" viewBox="0 0 28 28"><rect x="3" y="3" width="10" height="16" fill="none" stroke="#a32db4" stroke-width="2"/><path d="M8 7l-2 4h4l-2 4" stroke="#e0189a" stroke-width="1.5" fill="none"/><path d="M13 16h4l2-4h5l2 5v5H13z" fill="#a32db4"/></svg><h4>Installation</h4></div>
      <ul><li>Installation von Verkabelung und Elektrotechnik</li><li>Installation der Wallboxen</li><li>Setup der Abrechnungssysteme</li></ul>
    </div>
    <div class="step" style="top:405px">
      <div class="head"><svg width="28" height="28" viewBox="0 0 28 28"><path d="M4 18l3-6h14l3 6v5H4z" fill="#a32db4"/><circle cx="9" cy="19" r="1.6" fill="#fff"/><circle cx="19" cy="19" r="1.6" fill="#fff"/><path d="M8 4l12 8M20 4L8 12" stroke="#e0189a" stroke-width="1.8"/></svg><h4>Betrieb</h4></div>
      <ul><li>Technischer Betrieb</li><li>Abrechnung</li><li>Regelmäßige Wartung (DGUV3)</li><li>Anmeldung und Verwaltung neuer Nutzer</li><li>Anmeldung und Verwaltung neuer Nutzer</li></ul>
    </div>
  </div>
</section>

</body>
</html>
```